Zia Bortolo's Crostoli

Looking for a packaging Label for Italian cookies. It has started with my great grandmothers Pizzelle recipe. Recipe has been in the family for over 100 years.
The packaging will be either clear plastic bags or Clear plastic hinged containers. Hoping for something elegant but traditional Italian. I have attached the company logo for color and idea possibilities
Would also like to give donation to helping animal foundations

Target Market(s)

Cookie lovers, coffee and tea drinkers, lighter alternative to heavy cookies

Requirements
Nice to have
• Family, Italian tradition

```html
<!DOCTYPE html>
<html lang="en">
<head>
<meta charset="utf-8">
<title>Zia Bortolo's Crostoli – Label Designs</title>
<link href="https://fonts.googleapis.com/css2?family=Libre+Baskerville:wght@400;700&family=Pinyon+Script&display=swap" rel="stylesheet">
<style>
  :root {
    --backdrop: #c49a6c;
    --label-brown: #7a4a22;
    --label-orange: #f59a1f;
    --label-dark: #2c3532;
    --paper-white: #ffffff;
    --brand-orange: #e8662a;
    --seal-tan: #c9a57a;
    --tag-red: #d01f2e;
    --band-blue: #27a8e0;
    --flag-green: #009246;
    --flag-red: #ce2b37;
    --cookie-gold: #e08a2a;
    --cookie-light: #f3b35a;
  }
  html, body {
    margin: 0;
    width: 1200px;
    height: 1200px;
    overflow: hidden;
    background: var(--backdrop);
  }
  .label-sheet { display: block; width: 1200px; height: 1200px; }
  .serif { font-family: "Libre Baskerville", Georgia, serif; }
  .script { font-family: "Pinyon Script", cursive; }
  .product-title { font-weight: 700; font-size: 112px; letter-spacing: 2px; }
  .product-title-shadow { fill: var(--tag-red); }
  .product-title-main { fill: var(--paper-white); }
  .subtitle { fill: var(--label-orange); font-size: 84px; }
  .net-weight { fill: var(--seal-tan); font-size: 46px; }
  .net-weight-metric { fill: var(--seal-tan); font-size: 32px; }
  .origin-claim { fill: var(--seal-tan); font-size: 24px; }
  .seal-ring-text { fill: var(--seal-tan); font-size: 19px; letter-spacing: 3px; }
  .seal-number { fill: var(--seal-tan); font-size: 38px; font-weight: 700; }
  .tag-text { fill: var(--paper-white); font-size: 25px; font-weight: 700; }
  .flavour-name { fill: var(--paper-white); font-size: 56px; }
  .brand-name { fill: var(--brand-orange); font-size: 34px; font-weight: 400; }
</style>
</head>
<body>
<svg class="label-sheet" viewBox="0 0 2000 2000" xmlns="http://www.w3.org/2000/svg">
  <defs>
    <clipPath id="oval-inner"><ellipse cx="537" cy="980" rx="384" ry="440"/></clipPath>
    <clipPath id="square-inner"><rect x="1024" y="587" width="818" height="762" rx="12"/></clipPath>
    <path id="seal-arc-top-oval" d="M213,790 A62,62 0 0 1 337,790"/>
    <path id="seal-arc-bottom-oval" d="M205,790 A70,70 0 0 0 345,790"/>
    <path id="seal-arc-top-square" d="M1064,765 A66,66 0 0 1 1196,765"/>
    <path id="seal-arc-bottom-square" d="M1056,765 A74,74 0 0 0 1204,765"/>
  </defs>

  <!-- ===== Oval label ===== -->
  <g class="label label--oval">
    <ellipse cx="537" cy="980" rx="410" ry="466" fill="var(--label-brown)"/>
    <ellipse cx="537" cy="980" rx="396" ry="452" fill="none" stroke="var(--label-orange)" stroke-width="7" stroke-dasharray="6 4"/>
    <ellipse cx="537" cy="980" rx="384" ry="440" fill="var(--label-dark)"/>

    <g clip-path="url(#oval-inner)">
      <circle cx="545" cy="1345" r="250" fill="var(--cookie-gold)" role="img" aria-label="Golden patterned waffle cookie"/>
      <rect x="100" y="1205" width="900" height="65" fill="var(--band-blue)"/>
    </g>
    <text class="serif flavour-name" x="530" y="1256" text-anchor="middle">Vanilla</text>

    <path d="M372,515 H690 V805 Q630,812 605,850 Q570,832 531,842 Q492,832 457,850 Q432,812 372,805 Z" fill="var(--paper-white)" stroke="var(--label-orange)" stroke-width="8"/>
    <circle cx="531" cy="640" r="14" fill="none" stroke="var(--brand-orange)" stroke-width="3"/>
    <text class="serif brand-name" x="531" y="715" text-anchor="middle">Zia</text>
    <text class="serif brand-name" x="531" y="760" text-anchor="middle">Bortolo's</text>

    <g class="seal">
      <circle cx="275" cy="790" r="74" fill="none" stroke="var(--seal-tan)" stroke-width="2"/>
      <circle cx="275" cy="790" r="42" fill="none" stroke="var(--seal-tan)" stroke-width="2"/>
      <text class="serif seal-ring-text"><textPath href="#seal-arc-top-oval" startOffset="50%" text-anchor="middle">FAMILY RECIPE</textPath></text>
      <text class="serif seal-ring-text"><textPath href="#seal-arc-bottom-oval" startOffset="50%" text-anchor="middle" side="right">YEAR OLD</textPath></text>
      <text class="serif seal-number" x="275" y="803" text-anchor="middle">100</text>
    </g>

    <g class="flag">
      <rect x="741" y="588" width="28" height="157" fill="var(--flag-green)"/>
      <rect x="769" y="588" width="28" height="157" fill="var(--paper-white)"/>
      <rect x="797" y="588" width="28" height="157" fill="var(--flag-red)"/>
    </g>
    <text class="serif origin-claim" x="783" y="780" text-anchor="middle">AUTHENTIC</text>
    <text class="serif origin-claim" x="783" y="808" text-anchor="middle">ITALIAN</text>

    <text class="serif product-title product-title-shadow" x="514" y="991" text-anchor="middle">PIZZELLE</text>
    <text class="serif product-title product-title-main" x="522" y="985" text-anchor="middle">PIZZELLE</text>
    <text class="script subtitle" x="530" y="1048" text-anchor="middle">Italian waffle cookies</text>

    <text class="serif net-weight" x="278" y="1142" text-anchor="middle">7oz</text>
    <text class="serif net-weight-metric" x="280" y="1180" text-anchor="middle">(200g)</text>

    <g transform="rotate(-6 757 1125)">
      <rect x="652" y="1083" width="210" height="86" fill="var(--tag-red)"/>
      <text class="serif tag-text" x="757" y="1118" text-anchor="middle">HANDMADE</text>
      <text class="serif tag-text" x="757" y="1150" text-anchor="middle">DELICIOUS</text>
    </g>
  </g>

  <!-- ===== Square label ===== -->
  <g class="label label--square">
    <rect x="1000" y="565" width="865" height="805" rx="34" fill="var(--label-brown)"/>
    <rect x="1013" y="577" width="839" height="781" rx="22" fill="none" stroke="var(--label-orange)" stroke-width="7" stroke-dasharray="6 4"/>
    <rect x="1024" y="587" width="818" height="762" rx="12" fill="var(--label-dark)"/>

    <g clip-path="url(#square-inner)">
      <circle cx="1395" cy="1372" r="245" fill="var(--cookie-gold)" role="img" aria-label="Golden patterned waffle cookie"/>
      <rect x="1024" y="1205" width="818" height="66" fill="var(--band-blue)"/>
    </g>
    <text class="serif flavour-name" x="1405" y="1258" text-anchor="middle">Vanilla</text>

    <path d="M1243,565 H1563 V848 Q1503,855 1478,893 Q1443,875 1403,885 Q1363,875 1328,893 Q1303,855 1243,848 Z" fill="var(--paper-white)" stroke="var(--label-orange)" stroke-width="8"/>
    <circle cx="1403" cy="688" r="14" fill="none" stroke="var(--brand-orange)" stroke-width="3"/>
    <text class="serif brand-name" x="1403" y="763" text-anchor="middle">Zia</text>
    <text class="serif brand-name" x="1403" y="808" text-anchor="middle">Bortolo's</text>

    <g class="seal">
      <circle cx="1130" cy="765" r="78" fill="none" stroke="var(--seal-tan)" stroke-width="2"/>
      <circle cx="1130" cy="765" r="45" fill="none" stroke="var(--seal-tan)" stroke-width="2"/>
      <text class="serif seal-ring-text"><textPath href="#seal-arc-top-square" startOffset="50%" text-anchor="middle">FAMILY RECIPE</textPath></text>
      <text class="serif seal-ring-text"><textPath href="#seal-arc-bottom-square" startOffset="50%" text-anchor="middle" side="right">YEAR OLD</textPath></text>
      <text class="serif seal-number" x="1130" y="779" text-anchor="middle">100</text>
    </g>

    <g class="flag">
      <rect x="1627" y="588" width="28" height="159" fill="var(--flag-green)"/>
      <rect x="1655" y="588" width="28" height="159" fill="var(--paper-white)"/>
      <rect x="1683" y="588" width="28" height="159" fill="var(--flag-red)"/>
    </g>
    <text class="serif origin-claim" x="1668" y="786" text-anchor="middle" style="font-size:27px">AUTHENTIC</text>
    <text class="serif origin-claim" x="1668" y="820" text-anchor="middle" style="font-size:27px">ITALIAN</text>

    <text class="serif product-title product-title-shadow" x="1396" y="1014" text-anchor="middle" style="font-size:120px">PIZZELLE</text>
    <text class="serif product-title product-title-main" x="1404" y="1008" text-anchor="middle" style="font-size:120px">PIZZELLE</text>
    <text class="script subtitle" x="1400" y="1072" text-anchor="middle">Italian waffle cookies</text>

    <text class="serif net-weight" x="1124" y="1142" text-anchor="middle">7oz</text>
    <text class="serif net-weight-metric" x="1126" y="1180" text-anchor="middle">(200g)</text>

    <g transform="rotate(-6 1640 1130)">
      <rect x="1532" y="1086" width="216" height="88" fill="var(--tag-red)"/>
      <text class="serif tag-text" x="1640" y="1122" text-anchor="middle">HANDMADE</text>
      <text class="serif tag-text" x="1640" y="1155" text-anchor="middle">DELICIOUS</text>
    </g>
  </g>
</svg>
</body>
</html>
```